ターゲットは、墓地を探している方です。生前墓、小規模墓地、ペットと共に墓地に入れる敷地も用意されています。
http://www.asahidaireien.jp/
1ページ
緑 青
• イラストレーター形式 (.ai)
サイトレイアウトのPDFデータです。

弊社お客様にデザインを選んでいただきました。
お客様のイメージと一致したようでとても喜んでいただきました。

すばらしいデザインをありがとうございました。
24デザインの中からお客様に選んでいただきました。
お客様はとても喜んでおります。
今後ともよろしくお願いします。

```html
<!DOCTYPE html>
<html lang="ja">
<head>
<meta charset="utf-8">
<title>朝日台霊園</title>
<link href="https://fonts.googleapis.com/css2?family=Noto+Sans+JP:wght@400;700&family=Noto+Serif+JP:wght@500;700&display=swap" rel="stylesheet">
<style>
:root{
  --green:#3b8c3a;
  --green-dark:#2a6b2b;
  --green-light:#e9f3e0;
  --green-pale:#f4f9ef;
  --line:#9cc68f;
  --text:#333;
  --white:#fff;
}
*{box-sizing:border-box;margin:0;padding:0}
html,body{width:784px;height:1200px;overflow:hidden}
body{background:var(--white);font-family:"Noto Sans JP",sans-serif;color:var(--text);font-size:11px;line-height:1.6}
.page{width:784px;height:1200px;position:relative;border:1px solid var(--line)}
.header{height:92px;background:linear-gradient(var(--green),var(--green-dark));display:flex;justify-content:space-between;align-items:center;padding:0 28px;color:var(--white)}
.brand{display:flex;align-items:center;gap:10px}
.brand-mark{width:34px;height:34px;border-radius:50%;background:var(--white)}
.brand-tag{font-size:10px;letter-spacing:.1em}
.brand-name{font-family:"Noto Serif JP",serif;font-weight:700;font-size:26px;line-height:1.1}
.contact{text-align:right}
.contact-label{font-family:"Noto Serif JP",serif;font-size:14px}
.contact-tel{display:flex;align-items:center;gap:6px;font-size:27px;font-weight:700;letter-spacing:.02em;line-height:1.2}
.nav,.footer-nav{display:flex;background:var(--green);height:30px;margin:6px 8px 0}
.nav a,.footer-nav a{flex:1;color:var(--white);text-decoration:none;font-size:11px;display:flex;align-items:center;justify-content:center;border-right:1px solid var(--line)}
.nav a:last-child,.footer-nav a:last-child{border-right:none}
.hero{display:flex;height:214px;margin:6px 8px 0;gap:4px}
.hero-flowers{width:225px;background:linear-gradient(160deg,#d4458a,#b52d72 45%,#5c8a3c)}
.hero-grounds{flex:1;background:linear-gradient(180deg,#b9d3ef,#e4d2e6 30%,#9aa59b 55%,#6f7f66);position:relative}
.hero-copy{position:absolute;right:30px;top:22px;writing-mode:vertical-rl;font-family:"Noto Serif JP",serif;font-size:19px;color:var(--green-dark);line-height:1.7;background:rgba(255,255,255,.55);padding:8px 4px}
.content{display:flex;gap:12px;margin:14px 14px 0 18px}
.side{width:196px}
.side-head{background:var(--green);color:var(--white);font-family:"Noto Serif JP",serif;font-size:15px;text-align:center;height:32px;line-height:32px;border:2px solid var(--green-light);outline:1px solid var(--green)}
.voice{border:1px solid var(--line);padding:6px 10px;margin-bottom:10px}
.voice li{list-style:none;border-bottom:1px dotted var(--line);padding:2px 0;display:flex;gap:8px;font-size:11px}
.voice li:last-child{border:none}
.facilities{display:grid;grid-template-columns:repeat(4,1fr);gap:3px;border:1px solid var(--line);padding:6px;margin-bottom:10px}
.facilities span{font-size:10px;text-align:center;background:var(--green-pale);padding:4px 0}
.access-photo{height:96px;margin:6px 4px;background:linear-gradient(180deg,#c9dcee,#e6e6e0 50%,#8da07b)}
.access-note{font-size:9px;padding:0 6px;line-height:1.5}
.access-note strong{display:block;font-size:10px}
.info{width:100%;border-collapse:collapse;margin-top:6px;font-size:10px}
.info th{width:64px;text-align:left;font-weight:400;padding:4px 6px;border-bottom:1px dotted var(--line)}
.info td{padding:4px 4px;border-bottom:1px dotted var(--line)}
.main{flex:1}
.main-head{height:56px;border:1px solid var(--line);display:flex;align-items:center;background:linear-gradient(90deg,var(--green) 0,var(--green) 72%,#6f9c62 72%,#b4cfa6);color:var(--white);font-family:"Noto Serif JP",serif;font-size:21px;font-weight:700;padding-left:14px}
.intro{border:1px solid var(--line);border-top:none;padding:12px 16px;height:370px}
.intro p{margin-bottom:10px;font-size:11.5px;line-height:1.75}
.sub-head{margin-top:22px;height:38px;border:1px solid var(--line);display:flex;align-items:center;padding-left:12px;font-family:"Noto Serif JP",serif;font-size:16px;font-weight:700;color:var(--green-dark);background:linear-gradient(90deg,var(--green-pale) 70%,#c5d9bb)}
.sub-head::before{content:"";width:4px;height:20px;background:var(--green);margin-right:8px}
.sub-body{border:1px solid var(--line);border-top:none;padding:10px 14px;height:74px;font-size:10px}
.topics{list-style:none}
.topics li::before{content:"・";color:var(--green)}
.footer{position:absolute;left:0;right:0;bottom:0}
.footer-nav{margin:0 8px}
.copyright{text-align:center;font-size:9px;color:#666;height:26px;line-height:26px}
</style>
</head>
<body>
<div class="page">
  <header class="header">
    <div class="brand">
      <span class="brand-mark"></span>
      <div>
        <div class="brand-tag">やすらぎの公園墓地</div>
        <div class="brand-name">朝日台霊園</div>
      </div>
    </div>
    <div class="contact">
      <div class="contact-label">お問い合せは</div>
      <div class="contact-tel">
        <svg width="26" height="26" viewBox="0 0 24 24" aria-hidden="true"><path fill="#fff" d="M6.6 10.8a15.2 15.2 0 0 0 6.6 6.6l2.2-2.2c.3-.3.7-.4 1-.2 1.1.4 2.3.6 3.6.6.6 0 1 .4 1 1V20c0 .6-.4 1-1 1A17 17 0 0 1 3 4c0-.6.4-1 1-1h3.5c.6 0 1 .4 1 1 0 1.3.2 2.5.6 3.6.1.3 0 .7-.2 1z"/></svg>
        0120-00-4821
      </div>
    </div>
  </header>

  <nav class="nav">
    <a href="#">HOME</a><a href="#">墓地施設紹介</a><a href="#">地図・アクセス</a><a href="#">墓地申込</a><a href="#">お客様の声</a><a href="#">墓石紹介</a><a href="#">お問合せ</a>
  </nav>

  <section class="hero">
    <div class="hero-flowers" role="img" aria-label="満開の桃色の花の写真"></div>
    <div class="hero-grounds" role="img" aria-label="整然と並ぶ墓石と花木のある霊園の風景写真">
      <p class="hero-copy">やすらぎの<br>公園墓地</p>
    </div>
  </section>

  <div class="content">
    <aside class="side">
      <h2 class="side-head">お客様の声</h2>
      <ul class="voice">
        <li><span>宇都宮</span><span>鈴木様（仮名）</span></li>
        <li><span>東京都</span><span>山本様（仮名）</span></li>
        <li><span>日光市</span><span>鈴木様（仮名）</span></li>
      </ul>
      <h2 class="side-head">周辺施設</h2>
      <div class="facilities">
        <span>警察署</span><span>総合病院</span><span>公園</span><span>郵便局</span>
        <span>市役所</span><span>スーパー</span><span>消防署</span><span>図書館</span>
        <span>生花店</span><span>銀行</span><span>学校</span><span>駅</span>
      </div>
      <h2 class="side-head">アクセス</h2>
      <div class="access-photo" role="img" aria-label="霊園管理事務所の建物の写真"></div>
      <p class="access-note"><strong>朝日台インターより車5分</strong>国道沿いの案内看板を目印にお進みください。駐車場も広く、お車でのお参りも安心です。</p>
      <table class="info">
        <tr><th>名 称</th><td>朝日台霊園</td></tr>
        <tr><th>所在地</th><td>栃木県朝日台町1-2-3</td></tr>
        <tr><th>総面積</th><td>8,720㎡</td></tr>
        <tr><th>経営主体</th><td>宗教法人 朝日台寺</td></tr>
        <tr><th>事業主体</th><td>朝日台霊園管理事務所</td></tr>
        <tr><th>開 苑</th><td>平成元年5月</td></tr>
      </table>
    </aside>

    <main class="main">
      <h1 class="main-head">朝日台霊園について</h1>
      <div class="intro">
        <p>緑と陽光に包まれた永遠の安らぎを過ごすには非常に恵まれた最高の環境です。</p>
        <p>市街地から至近、通い慣れた方が来られても大丈夫（インターから5分以内で来られる便利な場所です。）</p>
        <p>法事会館（朝日台ホール・大駐車場）があります。30名・7年記帯の法事会場としてご利用できます。お食事もご用意しております。</p>
        <p>宗旨、宗派を問いません。どなたでも利用できます。（寄付金などありません）</p>
        <p>納骨のみの方、小規模墓地、ペットと共に眠れる区画もご用意しております。</p>
        <p>檀家制度はありませんので安心してお選びいただけます。</p>
        <p>ご予算、ご希望など承ります。お気軽にご相談ください。</p>
        <p>墓地、墓石のお求めにはローンや分割のご利用が出来ます。</p>
      </div>

      <h2 class="sub-head">霊園について</h2>
      <div class="sub-body">霊園の概要をご紹介します。</div>

      <h2 class="sub-head">トピックス</h2>
      <div class="sub-body"><ul class="topics"><li>ホームページを更新しました。</li></ul></div>
    </main>
  </div>

  <footer class="footer">
    <nav class="footer-nav">
      <a href="#">HOME</a><a href="#">墓地施設紹介</a><a href="#">地図・アクセス</a><a href="#">墓地申込</a><a href="#">お客様の声</a><a href="#">墓石紹介</a><a href="#">お問合せ</a>
    </nav>
    <p class="copyright">Copyright(C) asahidaireien.jp All Rights Reserved.</p>
  </footer>
</div>
</body>
</html>
```